Online-Marketing-Material für Reinigungsunternehmen
Zielgruppe
Wir sind ein seit Jahresanfang bestehende Reinigungsunternehmen.
Unsere Schwerpunkte liegen auf Treppenhausreinigung und Büroreinigung.
Die Anzeige soll auf Facebook / Instagram als Werbung angezeigt werden.
Kunden sind sowohl Unternehmer sowie auch Privathaushalte und Hausverwaltungen.
www.kolvaputz.de
Aufgabenstellung
Es darf gerne Modern und verspielt sein. Es soll und darf nicht billig wirken.
Wir haben auch ein Maskottchen. Es muss aber nicht auf die Anzeige mit drauf!

```html
<!DOCTYPE html>
<html lang="de">
<head>
<meta charset="utf-8">
<title>Kolva Putz – Anzeige</title>
<link rel="stylesheet" href="https://fonts.googleapis.com/css2?family=Poppins:wght@400;500;600;700;800&display=swap">
<style>
  :root {
    --blue-deep: #2f4f9c;
    --blue-head: #4561ad;
    --blue-head-light: #5874bb;
    --teal: #45b9ac;
    --white: #ffffff;
    --cta-blue: #3c7dc9;
    --cta-green: #6bbf3f;
    --photo-grey: #8a8a8c;
    --photo-yellow: #e6c545;
    --photo-skin: #c99577;
    --photo-plaid: #a8544f;
  }
  * { margin: 0; padding: 0; box-sizing: border-box; }
  html, body { width: 1200px; height: 1200px; overflow: hidden; background: var(--blue-deep); }
  .ad {
    position: relative;
    width: 1200px;
    height: 1200px;
    font-family: "Poppins", sans-serif;
    color: var(--white);
    overflow: hidden;
  }
  .hero-photo {
    position: absolute;
    left: 0; top: 0;
    width: 1200px; height: 886px;
    background:
      radial-gradient(ellipse 300px 340px at 780px 620px, var(--photo-skin) 0%, rgba(201,149,119,0.6) 55%, transparent 80%),
      radial-gradient(ellipse 260px 300px at 220px 620px, var(--photo-yellow) 0%, rgba(230,197,69,0.5) 60%, transparent 85%),
      linear-gradient(90deg, var(--photo-grey) 0%, #9b8f84 45%, var(--photo-plaid) 100%);
  }
  .headline-band {
    position: absolute;
    left: 0; top: 0;
    width: 1200px; height: 362px;
    background: linear-gradient(180deg, var(--blue-head) 0%, var(--blue-head-light) 100%);
  }
  .headline {
    position: absolute;
    left: 98px; top: 86px;
    font-weight: 800;
    line-height: 1;
    text-transform: uppercase;
  }
  .headline-top { display: block; font-size: 63px; letter-spacing: 0.5px; }
  .headline-main { display: block; font-size: 122px; margin-top: 14px; letter-spacing: -1px; }
  .brand {
    position: absolute;
    left: 98px; top: 628px;
    display: flex;
    align-items: center;
    gap: 22px;
  }
  .brand-mark { width: 48px; height: 48px; background: var(--white); }
  .brand-text { display: flex; flex-direction: column; }
  .brand-name { font-size: 62px; font-weight: 700; line-height: 1.05; }
  .brand-owner { font-size: 22px; font-weight: 400; margin-top: 8px; }
  .services-band {
    position: absolute;
    left: 0; top: 886px;
    width: 1200px; height: 111px;
    background: var(--teal);
    display: flex;
    align-items: center;
    padding-left: 98px;
    gap: 44px;
  }
  .service {
    display: flex;
    align-items: center;
    gap: 16px;
    font-size: 46px;
    font-weight: 600;
  }
  .service svg { width: 34px; height: 34px; }
  .footer {
    position: absolute;
    left: 0; top: 997px;
    width: 1200px; height: 203px;
    background: var(--blue-deep);
  }
  .footer-text {
    position: absolute;
    left: 98px; top: 50px;
    font-size: 29px;
    font-weight: 500;
    line-height: 1.62;
  }
  .cta {
    position: absolute;
    left: 872px; top: 66px;
    width: 230px; height: 72px;
    background: var(--white);
    border-radius: 7px;
    display: flex;
    align-items: center;
    justify-content: center;
    gap: 12px;
    color: var(--cta-blue);
    font-size: 33px;
    font-weight: 700;
    text-decoration: none;
  }
  .cta svg { width: 22px; height: 26px; }
</style>
</head>
<body>
<div class="ad">
  <div class="hero-photo" role="img" aria-label="Foto: lachende Frau mit Lockenwicklern, gelbem Gummihandschuh und Sprühflasche hinter einer eingeschäumten Glasscheibe"></div>

  <div class="headline-band">
    <h1 class="headline">
      <span class="headline-top">Schenken Sie Ihrem Objekt</span>
      <span class="headline-main">Neuen Glanz</span>
    </h1>
  </div>

  <div class="brand">
    <div class="brand-mark"></div>
    <div class="brand-text">
      <span class="brand-name">Kolva<br>Putz</span>
      <span class="brand-owner">Inh. Jonas Wellbrock</span>
    </div>
  </div>

  <div class="services-band">
    <div class="service">
      <svg viewBox="0 0 34 34"><path d="M4 18 L13 27 L30 8" fill="none" stroke="#fff" stroke-width="5" stroke-linecap="round" stroke-linejoin="round"/></svg>
      Treppenhausreinigung
    </div>
    <div class="service">
      <svg viewBox="0 0 34 34"><path d="M4 18 L13 27 L30 8" fill="none" stroke="#fff" stroke-width="5" stroke-linecap="round" stroke-linejoin="round"/></svg>
      Büroreinigung
    </div>
  </div>

  <div class="footer">
    <p class="footer-text">Zuverlässige, professionelle Reinigungskräfte<br>in den Kreisen Paderborn &amp; Gütersloh</p>
    <a class="cta" href="#">Anfragen
      <svg viewBox="0 0 22 26"><path d="M3 2 L12 2 L21 13 L12 24 L3 24 L12 13 Z" fill="var(--cta-green)"/></svg>
    </a>
  </div>
</div>
</body>
</html>
```